Flyer Design Dental Office Grand Opening offer

Dental office.

Grand opening flyer. Offer Exam + cleaning + xrays.
special: free teeth whitening ($200 value)

Target Market(s)

Middle class people around Huntington Beach.

Industry/Entity Type

Dental Clinic

Colors
cfeae6
86cfc6
fac994
fee18a
e667a6

Requirements
Must have
• Do not change my existing logo
Nice to have
• Have some appealing picture/design to catch the eye, but not too flashy
Should not have
• No cartoon kind of design

```html
<!DOCTYPE html>
<html lang="en">
<head>
<meta charset="utf-8">
<title>Sunrise Smile Dental – Grand Opening Flyer</title>
<link href="https://fonts.googleapis.com/css2?family=Anton&family=Bebas+Neue&family=Baloo+2:wght@600&family=Raleway:wght@400;500&family=Roboto:wght@400&family=Roboto+Condensed:wght@400&family=Lobster&display=swap" rel="stylesheet">
<style>
  :root{
    --backdrop:#1f5f8b;
    --paper:#ffffff;
    --teal:#2fb3c1;
    --teal-deep:#1e8f9c;
    --teal-soft:#86cfc6;
    --aqua-end:#6fcad2;
    --peach:#f9dccb;
    --ink:#1a1a1a;
    --orange:#ef6a2b;
    --cream:#efe9d6;
    --badge-green:#5d9e83;
    --badge-red:#9c3a22;
  }
  *{margin:0;padding:0;box-sizing:border-box}
  html,body{width:1200px;height:1200px;overflow:hidden}
  body{background:var(--backdrop);position:relative;font-family:"Roboto",sans-serif}

  .flyer{
    position:absolute;left:149px;top:20px;
    width:1002px;height:1289px;
    transform:scale(0.9);transform-origin:0 0;
    background:linear-gradient(180deg,var(--paper) 0%,var(--paper) 66%,#d7f0f1 80%,var(--aqua-end) 90%);
    overflow:hidden;
  }

  .photo{position:absolute;left:0;top:0;width:1002px;height:720px}

  .brand{position:absolute;left:0;top:62px;width:1002px;text-align:center}
  .brand-name{
    display:inline-flex;align-items:center;gap:14px;
    font-family:"Raleway",sans-serif;font-weight:500;font-size:52px;color:var(--teal-deep);
  }
  .brand-name .mark{width:36px;height:36px;background:var(--orange)}
  .dentist{position:absolute;right:302px;top:180px;font-size:17px;color:var(--ink)}
  .address{
    position:absolute;left:0;top:212px;width:1002px;text-align:center;
    font-family:"Roboto Condensed",sans-serif;font-size:25px;color:var(--ink);
  }

  .glow{
    position:absolute;left:330px;top:700px;width:400px;height:300px;
    background:radial-gradient(ellipse at center,rgba(250,150,90,.55) 0%,rgba(250,201,148,.25) 40%,rgba(255,255,255,0) 70%);
  }

  .tooth-art{position:absolute;left:65px;top:645px;width:230px;height:290px}

  .headline{position:absolute;left:290px;top:622px;width:560px;text-align:center}
  .headline .grand{
    display:block;font-family:"Raleway",sans-serif;font-weight:400;font-size:112px;line-height:96px;
    color:#fff;-webkit-text-stroke:3px var(--teal);letter-spacing:-2px;
  }
  .headline .opening{
    display:block;font-family:"Anton",sans-serif;font-size:168px;line-height:150px;
    color:#fff;-webkit-text-stroke:4px var(--teal);letter-spacing:-1px;
    text-shadow:0 4px 0 var(--teal-deep);
  }

  .badge{position:absolute;left:56px;top:930px;width:290px;height:225px}
  .badge-text{position:absolute;left:56px;top:930px;width:290px;height:225px;color:var(--badge-red)}
  .badge-text .special{position:absolute;left:20px;top:52px;font-family:"Lobster",cursive;font-size:48px;transform:rotate(-16deg)}
  .badge-text .offer{position:absolute;left:78px;top:98px;font-family:"Lobster",cursive;font-size:48px;transform:rotate(-16deg)}
  .badge-text .value{position:absolute;left:130px;top:150px;font-family:"Bebas Neue",sans-serif;font-size:32px;color:var(--ink);transform:rotate(-16deg)}

  .includes{
    position:absolute;left:364px;top:936px;
    font-family:"Baloo 2",sans-serif;font-weight:600;font-size:44px;color:var(--ink);white-space:nowrap;
  }
  .free{
    position:absolute;left:358px;top:982px;
    font-family:"Anton",sans-serif;font-size:138px;line-height:140px;color:#fff;letter-spacing:2px;
  }
  .brace{position:absolute;left:610px;top:990px;width:40px;height:130px}
  .whitening{
    position:absolute;left:668px;top:998px;
    font-family:"Bebas Neue",sans-serif;font-size:64px;line-height:60px;color:#fff;
  }

  .call-band{
    position:absolute;left:0;top:1167px;width:1002px;height:76px;background:var(--peach);
    display:flex;align-items:center;justify-content:center;
    font-family:"Bebas Neue",sans-serif;font-size:50px;letter-spacing:2px;color:var(--ink);
  }
  .call-band .phone{margin-left:22px}
  .foot-band{position:absolute;left:0;top:1243px;width:1002px;height:46px;background:#3db8c8}
</style>
</head>
<body>
  <div class="flyer">
    <svg class="photo" viewBox="0 0 1002 720" role="img" aria-label="Photo of a smiling dentist in scrubs holding up a dental x-ray">
      <defs>
        <linearGradient id="photoTone" x1="0" y1="0" x2="1" y2="1">
          <stop offset="0" stop-color="#f1f5f7"/>
          <stop offset="0.45" stop-color="#dfe8ec"/>
          <stop offset="0.75" stop-color="#b9c9d3"/>
          <stop offset="1" stop-color="#e6eef2"/>
        </linearGradient>
      </defs>
      <path d="M0 330 Q501 200 1002 330 L1002 688 Q520 600 0 640 Z" fill="url(#photoTone)"/>
    </svg>

    <div class="brand">
      <span class="brand-name"><span class="mark"></span>Sunrise Smile Dental</span>
    </div>
    <div class="dentist">Lena Haroldsen, DDS</div>
    <div class="address">1847 Larkmoor Ave., Huntington Beach, CA 92647</div>

    <div class="glow"></div>

    <svg class="tooth-art" viewBox="0 0 230 290" role="img" aria-label="Illustration of a white tooth with a dental mirror, probe and green leaves">
      <defs>
        <linearGradient id="toothTone" x1="0" y1="0" x2="0" y2="1">
          <stop offset="0" stop-color="#f7f9fa"/>
          <stop offset="1" stop-color="#d6dde1"/>
        </linearGradient>
      </defs>
      <rect x="0" y="0" width="230" height="290" rx="30" fill="url(#toothTone)"/>
    </svg>

    <div class="headline">
      <span class="grand">GRAND</span>
      <span class="opening">OPENING</span>
    </div>

    <svg class="badge" viewBox="0 0 290 225" aria-hidden="true">
      <path d="M40 20 H250 L270 50 V175 L250 205 H40 L20 175 V50 Z" fill="var(--badge-green)"/>
      <path d="M48 30 H242 L258 56 V169 L242 195 H48 L32 169 V56 Z" fill="var(--cream)"/>
      <path d="M56 40 H234 L248 62 V163 L234 185 H56 L42 163 V62 Z" fill="none" stroke="#b9ae92" stroke-width="1.5" stroke-dasharray="5 4"/>
    </svg>
    <div class="badge-text">
      <span class="special">Special</span>
      <span class="offer">Offer</span>
      <span class="value">$200 VALUE</span>
    </div>

    <div class="includes">Exam + cleaning + xrays</div>
    <div class="free">FREE</div>
    <svg class="brace" viewBox="0 0 40 130" aria-hidden="true">
      <path d="M6 4 Q22 4 20 30 Q18 60 34 65 Q18 70 20 100 Q22 126 6 126" fill="none" stroke="#fff" stroke-width="3"/>
    </svg>
    <div class="whitening">TEETH<br>WHITENING</div>

    <div class="call-band">CALL US NOW <span class="phone">(714) 555-0186</span></div>
    <div class="foot-band"></div>
  </div>
</body>
</html>
```